"Brelunda" sparkling beverage

Dear All!
I need a stick label (82*95 - front label, 82*65 - back label )design for а sparkling beverage, name is "Brelunda", 4 flavours: lemonade,duchess pear, estragon, original. Transparent glass bottles 0,5 liter (alumnium closure 28*15)/0,33 liter (crown cap), neck label should also be on the bottle 0,5 liter.
European style is welcomed
Do not send the disigns with a little changes several times, please!!!
Target Market(s)
Young people from 12-30 ages old
Look and feel
Each slider illustrates characteristics of the customer's brand and the style your logo design should communicate.

```html
<!DOCTYPE html>
<html lang="en">
<head>
<meta charset="utf-8">
<title>Brelunda sparkling beverage front labels</title>
<link rel="stylesheet" href="https://fonts.googleapis.com/css2?family=Montserrat:wght@700;800&family=Quicksand:wght@300&display=swap">
<style>
  :root {
    --backdrop: #c8c7c8;
    --label: #f7f7f6;
    --ink: #141414;
    --lemon-main: #f2e22a;
    --lemon-deep: #d9c90f;
    --pear-main: #59b83a;
    --pear-deep: #2f8a2a;
  }
  * { box-sizing: border-box; margin: 0; padding: 0; }
  html, body {
    width: 1200px;
    height: 1146px;
    overflow: hidden;
    background: var(--backdrop);
  }
  .label-row {
    position: absolute;
    left: 0;
    top: 0;
    width: 1200px;
    height: 1146px;
    display: flex;
    justify-content: center;
    align-items: center;
    gap: 80px;
  }
  .front-label {
    width: 420px;
    height: 486px;
    background: var(--label);
    display: flex;
    flex-direction: column;
    align-items: center;
    padding-top: 40px;
    box-shadow: 0 2px 10px rgba(0,0,0,0.08);
  }
  .product-type {
    font-family: "Montserrat", sans-serif;
    font-weight: 800;
    font-size: 15px;
    letter-spacing: 0.2px;
    color: var(--ink);
  }
  .brand-name {
    font-family: "Montserrat", sans-serif;
    font-weight: 800;
    font-size: 46px;
    letter-spacing: 0.5px;
    color: var(--ink);
    line-height: 1;
    margin-top: 6px;
  }
  .flavour-art {
    width: 300px;
    height: 240px;
    margin-top: 8px;
    border-radius: 48% 52% 44% 56% / 55% 45% 55% 45%;
  }
  .flavour-art--lemon {
    background: radial-gradient(ellipse at 50% 50%, var(--lemon-main) 0%, var(--lemon-deep) 55%, rgba(242,226,42,0) 75%);
  }
  .flavour-art--pear {
    background: radial-gradient(ellipse at 50% 50%, var(--pear-main) 0%, var(--pear-deep) 55%, rgba(89,184,58,0) 75%);
  }
  .flavour-name {
    font-family: "Quicksand", sans-serif;
    font-weight: 300;
    font-size: 40px;
    color: var(--ink);
    line-height: 1;
    margin-top: -36px;
    padding-bottom: 6px;
    border-bottom: 3px solid var(--ink);
  }
</style>
</head>
<body>
  <main class="label-row">
    <section class="front-label">
      <p class="product-type">SPARKLING BEVERAGE</p>
      <h1 class="brand-name">BRELUNDA</h1>
      <div class="flavour-art flavour-art--lemon" role="img" aria-label="Yellow watercolour splash with a white lemon slice icon"></div>
      <p class="flavour-name">lemonade</p>
    </section>
    <section class="front-label">
      <p class="product-type">SPARKLING BEVERAGE</p>
      <h1 class="brand-name">BRELUNDA</h1>
      <div class="flavour-art flavour-art--pear" role="img" aria-label="Green watercolour splash with a white pear icon"></div>
      <p class="flavour-name">duchess pear</p>
    </section>
  </main>
</body>
</html>
```